Flyer-Design für Import von griechischem Premium-Olivenöl
Zielgruppe
Direktimport von griechischem Premium Olivenöl aus Zakynthos
Versand an Privatkunden in Österreich und Deutschland via Web-Shop www.kelmar-fett.at
Aufgabenstellung
Traditionelle Herstellung von hochwertigem Olivenöl
Direktimport vom Erzeuger
Bio-Olivenöl oder gemeinsam mit frischen, ungespritzen Zitronen, Orangen oder Knoblauch gepresst.
Flyer soll das Natürliche, ehrliche Handwerk betonen, nur Koroneiki Oliven der Insel Zakynthos werden verwendet, nichts wird gepanscht vermischt
Wunschformat C6

```html
<!DOCTYPE html>
<html lang="de">
<head>
<meta charset="utf-8">
<title>Oliven Öl Premium – Flyer</title>
<link rel="stylesheet" href="https://fonts.googleapis.com/css2?family=Courgette&family=Sansita:ital,wght@0,700;1,800&family=Playfair+Display:wght@600&display=swap">
<style>
  :root {
    --olive: #6e7b2f;
    --olive-dark: #5a6624;
    --olive-soft: #a7ae7a;
    --paper: #e4e4e2;
    --paper-light: #f1f1ef;
    --oil: #d9a827;
    --oil-deep: #b07d12;
    --gold: #e7c766;
    --gold-edge: #c79a2a;
  }
  * { margin: 0; padding: 0; box-sizing: border-box; }
  html, body { width: 844px; height: 1200px; overflow: hidden; background: var(--paper); }
  .flyer {
    position: relative;
    width: 844px;
    height: 1200px;
    overflow: hidden;
    background: radial-gradient(ellipse at 60% 45%, var(--paper-light) 0%, var(--paper) 70%);
  }
  .flyer__waves { position: absolute; inset: 0; width: 844px; height: 1200px; }
  .flyer__title {
    position: absolute;
    top: 42px;
    left: 0;
    width: 844px;
    text-align: center;
    font-family: "Courgette", cursive;
    font-weight: 400;
    font-size: 128px;
    line-height: 1.1;
    color: var(--olive);
    z-index: 2;
  }
  .flyer__subtitle {
    position: absolute;
    top: 208px;
    left: 0;
    width: 844px;
    text-align: center;
    font-family: "Playfair Display", serif;
    font-weight: 600;
    font-size: 40px;
    letter-spacing: 3px;
    color: var(--olive-dark);
    z-index: 2;
  }
  .bottle-photo {
    position: absolute;
    left: 0;
    top: 235px;
    width: 340px;
    height: 965px;
    background:
      radial-gradient(ellipse at 45% 12%, #e9e2cc 0%, rgba(233,226,204,0) 40%),
      linear-gradient(180deg, #d7d2c2 0%, #cfc7ae 28%, var(--oil) 42%, var(--oil-deep) 100%);
    border-radius: 60px 140px 0 0;
    opacity: 0.9;
  }
  .claim { position: absolute; left: 390px; top: 290px; width: 440px; color: var(--olive); z-index: 2; }
  .claim__percent {
    font-family: "Sansita", sans-serif;
    font-style: italic;
    font-weight: 800;
    font-size: 168px;
    line-height: 1;
    text-align: center;
  }
  .claim__text {
    font-family: "Sansita", sans-serif;
    font-weight: 700;
    font-size: 80px;
    line-height: 0.98;
    padding-left: 54px;
    margin-top: 12px;
  }
  .olive-bowl {
    position: absolute;
    left: 335px;
    top: 740px;
    width: 509px;
    height: 390px;
    background: radial-gradient(ellipse at 55% 55%, var(--olive-soft) 0%, rgba(167,174,122,0.55) 45%, rgba(167,174,122,0) 75%);
  }
  .origin-label {
    position: absolute;
    left: 606px;
    top: 1058px;
    width: 225px;
    height: 104px;
    border-radius: 14px;
    background: linear-gradient(180deg, #f3dc8d 0%, var(--gold) 100%);
    border: 4px solid var(--gold-edge);
    display: flex;
    align-items: center;
    justify-content: center;
    text-align: center;
    font-family: "Courgette", cursive;
    font-size: 24px;
    line-height: 1.2;
    color: var(--olive-dark);
    z-index: 2;
  }
</style>
</head>
<body>
  <main class="flyer">
    <svg class="flyer__waves" viewBox="0 0 844 1200" aria-hidden="true">
      <path d="M0 0 H360 C220 8 100 22 0 48 Z" fill="var(--olive-soft)" opacity="0.55"/>
      <path d="M300 1200 C520 1120 700 1010 844 880 V1200 Z" fill="var(--olive)" opacity="0.85"/>
      <path d="M260 1200 C500 1105 690 990 844 850 V880 C700 1010 520 1120 300 1200 Z" fill="var(--olive-soft)" opacity="0.6"/>
    </svg>

    <h1 class="flyer__title">Oliven Öl</h1>
    <p class="flyer__subtitle">· PREMIUM ·</p>

    <div class="bottle-photo" role="img" aria-label="Foto: Glaskaraffe mit goldenem Olivenöl und Korken"></div>

    <div class="claim">
      <p class="claim__percent">100%</p>
      <p class="claim__text">Handmade<br>&amp; Bio</p>
    </div>

    <div class="olive-bowl" role="img" aria-label="Illustration: Schale mit grünen Oliven und Olivenzweig"></div>

    <p class="origin-label">Koroneiki Oliven<br>aus Zakynthos</p>
  </main>
</body>
</html>
```